prestige web design for KELVA Finance

Hi Guys,

Looking to team up with a creative designer for another of our websites for KELVA finance.
if looking for our similar website www.brimlendco.com.au is one of our other companies. ideally working in our logo being black and white.

Please see attachments for our logo and a description
HOME
VEHICLE
EQUIPMENT
WHO WE ARE
CONTACT US

open to ideas on layout .

touch base if you have any questions.

Target Market(s)

Prestige cars and equipment -trucks earthmoving

Industry/Entity Type

finance

Coding

Coded - Design and coding required

Number of Pages Required

5+ page

Font styles to use
Sans Serif

Colors

Designer to choose colors to be used in the design.

```html
<!DOCTYPE html>
<html lang="en">
<head>
<meta charset="utf-8">
<title>KELVA Finance</title>
<link href="https://fonts.googleapis.com/css2?family=Montserrat:wght@400;500;600;700;800&display=swap" rel="stylesheet">
<style>
:root{
  --ink:#1a1a1a;
  --text:#333;
  --muted:#777;
  --line:#bdbdbd;
  --paper:#ffffff;
  --dark:#2a2a2a;
  --night:#1f1f1f;
  --accent:#f7a21b;
}
*{box-sizing:border-box;margin:0;padding:0}
html,body{width:1200px;height:3983px;overflow:hidden}
body{position:relative;background:var(--paper);font-family:'Montserrat',sans-serif;color:var(--text)}
.abs{position:absolute}
.nowrap{white-space:nowrap}
.site-header{top:0;left:0;width:1200px;height:90px;background:var(--paper)}
.brand{font-family:'Montserrat',sans-serif;font-weight:800;color:var(--ink);white-space:nowrap}
.site-header .brand{left:85px;top:26px;font-size:32px;letter-spacing:-0.5px}
.main-nav a{position:absolute;top:38px;font-size:13px;color:var(--ink);text-decoration:none;font-weight:500}
.main-nav a.active{font-weight:700}
.header-phone{left:1002px;top:35px;font-size:14px;font-weight:700;color:var(--ink);display:flex;align-items:center;gap:6px}
.hero-bg{top:90px;left:0;width:1200px;height:624px;background:linear-gradient(90deg,#e9e9e9,#f4f4f4 40%,#dcdcdc)}
.hero-photo{top:90px;left:456px;width:744px;height:624px;clip-path:polygon(217px 0,744px 0,744px 624px,0 624px);background:linear-gradient(160deg,#f0d9a8 0%,#c6a172 30%,#9a8b7c 55%,#6d5a43 80%,#3f3326 100%)}
.hero-title{left:93px;top:272px;font-size:68px;line-height:70px;font-weight:800;color:var(--ink);letter-spacing:-1px;white-space:nowrap}
.hero-sub{left:98px;top:420px;font-size:19px;line-height:30px;color:var(--ink);white-space:nowrap}
.scroll{left:108px;top:526px;font-size:13px;letter-spacing:3px;color:var(--ink);font-weight:500}
.calc{top:674px;left:90px;width:1000px;height:254px;background:#f7f7f7;border:1px solid #d8d8d8}
.calc h2{position:absolute;left:43px;top:38px;font-size:23px;font-weight:600;color:var(--ink)}
.field{position:absolute;width:278px;border-bottom:2px solid var(--line);padding-bottom:6px}
.field .lbl{font-size:12px;color:var(--muted);display:block;margin-bottom:6px}
.field .val{font-size:16px;font-weight:600;color:var(--ink)}
.btn-calc{position:absolute;left:676px;top:161px;width:276px;height:45px;background:var(--accent);color:#fff;font-size:16px;font-weight:700;letter-spacing:2px;display:flex;align-items:center;justify-content:center;gap:8px}
.intro-title{left:0;width:1200px;top:1002px;text-align:center;font-size:41px;font-weight:800;color:var(--ink);letter-spacing:-1px}
.rule{height:2px;background:var(--ink)}
.intro-text{left:0;width:1200px;text-align:center;font-size:17.5px;line-height:25px;color:var(--text);white-space:nowrap}
.vehicle{top:1385px;left:0;width:1200px;height:512px;background:linear-gradient(120deg,#3b3b3b,#262626 60%,#1c1c1c)}
.vehicle-photo{top:1385px;left:0;width:665px;height:512px;clip-path:polygon(0 0,448px 0,665px 512px,0 512px);background:linear-gradient(180deg,#a7aeb8 0%,#cfd2d4 35%,#e8e8e8 55%,#b8ab98 80%,#8f8270 100%)}
.band-title{font-size:40px;font-weight:800;letter-spacing:-1px;white-space:nowrap}
.band-text{font-size:17.5px;line-height:29px;white-space:nowrap}
.btn-outline{display:flex;align-items:center;justify-content:center;font-size:13px;font-weight:700;letter-spacing:1.5px;border:2px solid}
.equip{top:1898px;left:0;width:1200px;height:511px;background:linear-gradient(90deg,#f2f2f2,#e6e6e6 60%,#d9d9d9)}
.equip-photo{top:1898px;left:464px;width:736px;height:511px;clip-path:polygon(162px 0,736px 0,736px 511px,0 511px);background:linear-gradient(180deg,#7fb0e0 0%,#c9dff2 30%,#d8b88e 55%,#b99466 78%,#9c7b55 100%)}
.equip-text{left:110px;top:2098px;font-size:16px;line-height:25px;color:var(--ink);white-space:nowrap}
.about-frame{top:2514px;left:83px;width:537px;height:411px;border:2px solid #cfcfcf;background:#fff}
.about-photo{top:2522px;left:93px;width:519px;height:394px;background:linear-gradient(160deg,#e6c48c 0%,#b58a55 35%,#6b5742 65%,#3d3126 100%)}
.about-title{left:719px;top:2546px;font-size:34px;font-weight:800;color:var(--ink);letter-spacing:-0.5px}
.about-text{left:719px;top:2610px;font-size:14.5px;line-height:25px;color:var(--ink);white-space:nowrap}
.contact{top:3031px;left:0;width:1200px;height:652px;background:linear-gradient(90deg,#050505 0,#050505 97px,#2e2e2e 97px,#3a3a3a 55%,#262626 100%)}
.contact-title{left:0;width:1200px;top:3095px;text-align:center;font-size:38px;font-weight:800;color:#fff;letter-spacing:-1px}
.contact-lead{left:0;width:1200px;top:3168px;text-align:center;font-size:16.5px;line-height:24px;color:#eee;white-space:nowrap}
.input{background:#fff;border:1px solid #ccc;font-size:13px;color:#777;padding:0 22px;display:flex;align-items:center}
.input.msg{align-items:flex-start;padding-top:14px}
.site-footer .brand{left:100px;top:3726px;font-size:40px;letter-spacing:-0.5px}
.foot-item{display:flex;align-items:center;gap:14px}
.foot-item .cap{font-size:12px;color:var(--text);display:block}
.foot-item .v{font-size:13px;font-weight:700;color:var(--ink);display:block;margin-top:4px;white-space:nowrap}
.hline{height:1px;background:#e3e3e3;left:0;width:1200px}
.foot-nav a{position:absolute;top:3864px;font-size:15px;color:var(--ink);text-decoration:none;font-weight:500;transform:translateX(-50%);white-space:nowrap}
.copy{left:0;width:1142px;top:3942px;text-align:center;font-size:11px;color:var(--text)}
.to-top{left:1023px;top:3930px;width:34px;height:34px;border-radius:50%;background:var(--night);display:flex;align-items:center;justify-content:center}
</style>
</head>
<body>

<header class="abs site-header">
  <div class="abs brand">KELVA Finance</div>
  <nav class="main-nav">
    <a class="active" style="left:385px">HOME</a>
    <a style="left:476px">VEHICLE</a>
    <a style="left:583px">EQUIPMENT</a>
    <a style="left:713px">WHO WE ARE</a>
    <a style="left:850px">CONTACT US</a>
  </nav>
  <div class="abs header-phone">
    <svg width="16" height="16" viewBox="0 0 24 24"><path fill="#1a1a1a" d="M6.6 10.8a15.1 15.1 0 0 0 6.6 6.6l2.2-2.2a1 1 0 0 1 1-.25 11.4 11.4 0 0 0 3.6.57 1 1 0 0 1 1 1V20a1 1 0 0 1-1 1A17 17 0 0 1 3 4a1 1 0 0 1 1-1h3.5a1 1 0 0 1 1 1c0 1.25.2 2.45.57 3.57a1 1 0 0 1-.25 1z"/></svg>
    1300 418 2275
  </div>
</header>

<section class="abs hero-bg" role="img" aria-label="Faded photo of a mining truck"></section>
<div class="abs hero-photo" role="img" aria-label="Photo of a silver luxury SUV on a dusty hillside at sunset"></div>
<h1 class="abs hero-title">MAKERS OF<br>POSSIBLE</h1>
<p class="abs hero-sub">KELVA Finance has nearly 20 years<br>industry experience</p>
<div class="abs scroll">SCROLL</div>
<svg class="abs" style="left:124px;top:552px" width="32" height="20" viewBox="0 0 32 20"><path d="M3 3l13 13L29 3" fill="none" stroke="#1a1a1a" stroke-width="3.5"/></svg>

<section class="abs calc">
  <h2>FINANCE REPAYMENT CALCULATOR</h2>
  <div class="field" style="left:44px;top:88px"><span class="lbl">Purchase amount</span><span class="val">$100000</span></div>
  <div class="field" style="left:343px;top:88px"><span class="lbl">Deposit</span><span class="val">$5000</span></div>
  <div class="field" style="left:675px;top:86px;width:276px"><span class="lbl">Balloon Payment</span><span class="val">$2000</span></div>
  <div class="field" style="left:44px;top:154px"><span class="lbl">Term</span><span class="val">5 Year</span></div>
  <div class="field" style="left:343px;top:161px"><span class="lbl">Interest rate% pa.</span><span class="val">7.5</span></div>
  <div class="btn-calc">CALCULATE
    <svg width="20" height="14" viewBox="0 0 20 14"><path d="M1 7h16M12 2l5 5-5 5" fill="none" stroke="#fff" stroke-width="2"/></svg>
  </div>
</section>

<section class="intro">
  <h2 class="abs intro-title">MAKERS OF POSSIBLE</h2>
  <div class="abs rule" style="left:561px;top:1059px;width:78px"></div>
  <p class="abs intro-text" style="top:1097px">KELVA Finance has nearly 20 years industry experience, so we certainly understand personal<br>and business lending. We are committed to providing individuals and businesses with tailored<br>financial services that enable them to reach and then exceed their financial goals.</p>
  <p class="abs intro-text" style="top:1197px">We have a vast list of lenders to suit along with an online team ready to help you, so we're<br>easily accessible and here when you need us. Our friendly team of experienced and approach-<br>able staff that will listen, understand your situation and lend responsibly.</p>
</section>

<section class="abs vehicle" role="img" aria-label="Dark photo of a car interior"></section>
<div class="abs vehicle-photo" role="img" aria-label="Photo of a white luxury SUV parked on a city lot"></div>
<h2 class="abs band-title" style="left:696px;top:1540px;color:#fff">VEHICLE LOAN</h2>
<p class="abs band-text" style="left:707px;top:1604px;color:#eee">While you focus on getting the right car, we<br>will focus on getting you the right finance.</p>
<div class="abs btn-outline" style="left:707px;top:1684px;width:151px;height:41px;color:#fff;border-color:#fff">APPLY NOW</div>

<section class="abs equip" role="img" aria-label="Faded photo of an excavator"></section>
<div class="abs equip-photo" role="img" aria-label="Photo of a yellow wheel loader at a sand quarry beside a tipper truck"></div>
<h2 class="abs band-title" style="left:108px;top:2036px;color:var(--ink)">EQUIPMENT</h2>
<p class="abs equip-text">At KELVA, we help businesses of all<br>sizes to secure funding in the form of a<br>business loan for asset purchases from<br>either a bank or private lender.</p>
<div class="abs btn-outline" style="left:111px;top:2225px;width:150px;height:42px;color:var(--ink);border-color:var(--ink)">APPLY NOW</div>

<section class="about">
  <div class="abs about-frame"></div>
  <div class="abs about-photo" role="img" aria-label="Photo of a grey premium SUV on a hillside at golden hour"></div>
  <h2 class="abs about-title">WHO WE ARE</h2>
  <p class="abs about-text">The goal of KELVA Finance is to build on the track record<br>of the KELVA business and to create a new benchmark in<br>the Australia's Asset Finance industry, providing good old<br>fashioned localised service that delivers the assets you<br>want when you need them and structured to recognise<br>asset useful life while being sensitive to cashflow.</p>
  <div class="abs btn-outline" style="left:719px;top:2785px;width:164px;height:46px;color:var(--ink);border-color:var(--ink)">LEARN MORE</div>
</section>

<section class="abs contact" role="img" aria-label="Dark photo of a city skyline"></section>
<h2 class="abs contact-title">CONTACT US</h2>
<p class="abs contact-lead">To find out how to get KELVA Finance working for you helping with your funding needs.<br>Please call 13 55 88 &nbsp;( 13 KELVA ) &nbsp;Or Contact us now: Alternatively send us a message with your questions.</p>
<div class="abs input" style="left:247px;top:3260px;width:364px;height:44px">First Name*</div>
<div class="abs input" style="left:625px;top:3260px;width:362px;height:44px">Last Name*</div>
<div class="abs input" style="left:247px;top:3314px;width:364px;height:44px">Email*</div>
<div class="abs input" style="left:625px;top:3314px;width:362px;height:44px">Phone*</div>
<div class="abs input" style="left:247px;top:3370px;width:364px;height:45px">Location</div>
<div class="abs input" style="left:625px;top:3370px;width:362px;height:45px">Subject</div>
<div class="abs input msg" style="left:247px;top:3427px;width:740px;height:96px">Message</div>
<div class="abs btn-outline" style="left:518px;top:3540px;width:193px;height:51px;color:#fff;border-color:#fff">SEND MESSAGE</div>

<footer class="site-footer">
  <div class="abs brand">KELVA Finance</div>
  <div class="abs foot-item" style="left:459px;top:3736px">
    <svg width="32" height="32" viewBox="0 0 32 32"><circle cx="16" cy="16" r="16" fill="#8a8a8a"/><path transform="translate(8 8) scale(.67)" fill="#fff" d="M6.6 10.8a15.1 15.1 0 0 0 6.6 6.6l2.2-2.2a1 1 0 0 1 1-.25 11.4 11.4 0 0 0 3.6.57 1 1 0 0 1 1 1V20a1 1 0 0 1-1 1A17 17 0 0 1 3 4a1 1 0 0 1 1-1h3.5a1 1 0 0 1 1 1c0 1.250.2 2.450.57 3.57a1 1 0 0 1-.25 1z"/></svg>
    <div><span class="cap">PHONE</span><span class="v">(123) 555 0142</span></div>
  </div>
  <div class="abs foot-item" style="left:646px;top:3736px">
    <svg width="32" height="32" viewBox="0 0 32 32"><circle cx="16" cy="16" r="16" fill="#8a8a8a"/><rect x="9" y="11" width="14" height="10" fill="none" stroke="#fff" stroke-width="1.6"/><path d="M9 11l7 6 7-6" fill="none" stroke="#fff" stroke-width="1.6"/></svg>
    <div><span class="cap">EMAIL</span><span class="v">enquiry@kelvafin.com</span></div>
  </div>
  <div class="abs foot-item" style="left:883px;top:3736px">
    <svg width="32" height="32" viewBox="0 0 32 32"><circle cx="16" cy="16" r="16" fill="#8a8a8a"/><path d="M16 8a5.5 5.5 0 0 0-5.5 5.5C10.5 18 16 24 16 24s5.5-6 5.5-10.5A5.5 5.5 0 0 0 16 8z" fill="#fff"/><circle cx="16" cy="13.5" r="2" fill="#8a8a8a"/></svg>
    <div><span class="cap">LOCATION</span><span class="v">48 Harbour Lane</span></div>
  </div>
  <div class="abs hline" style="top:3830px"></div>
  <nav class="foot-nav">
    <a style="left:278px">HOME</a>
    <a style="left:420px">VEHICLE</a>
    <a style="left:585px">EQUIPMENT</a>
    <a style="left:768px">WHO WE ARE</a>
    <a style="left:956px">CONTACT US</a>
  </nav>
  <div class="abs hline" style="top:3915px"></div>
  <div class="abs copy">© 2022 KELVA Finance | All Right Reserved</div>
  <div class="abs to-top"><svg width="14" height="10" viewBox="0 0 14 10"><path d="M1 8l6-6 6 6" fill="none" stroke="#fff" stroke-width="2"/></svg></div>
</footer>

</body>
</html>
```